Harrowgate Supply Group Business Card Design

The Business Card will be one side only with Harrowgate Supplies Group Logo
Card should have:
Name
Title
Office phone Number
Cell Number
email address
Website
Ironwood Street
Our Slogan is Tough and Dependable
Looking for something that stands out from other business cards

Target Market(s)

Heavy equipment Lease Company

```html
<!DOCTYPE html>
<html lang="en">
<head>
<meta charset="utf-8">
<title>Harrowgate Supplies Group – Business Card</title>
<link rel="stylesheet" href="https://fonts.googleapis.com/css2?family=Arimo:wght@400;700&display=swap">
<style>
  :root {
    --backdrop: #2b2b2b;
    --card: #ffffff;
    --red: #d0202f;
    --navy: #2a2c7c;
    --grey-text: #5a5a5a;
    --map-tone: #eeeef1;
  }
  * { margin: 0; padding: 0; box-sizing: border-box; }
  html, body { width: 1200px; height: 880px; overflow: hidden; }
  body {
    background: var(--backdrop);
    font-family: "Arimo", Arial, sans-serif;
    position: relative;
  }
  .card {
    position: absolute;
    left: 250px;
    width: 700px;
    height: 400px;
    background: var(--card);
    border-radius: 22px;
    overflow: hidden;
  }
  .card-back { top: 20px; }
  .card-front { top: 460px; }

  /* Back side */
  .world-map {
    position: absolute;
    left: 120px; top: 40px;
    width: 520px; height: 320px;
    border-radius: 40% 50% 45% 55%;
    background: radial-gradient(ellipse at center, var(--map-tone) 0%, rgba(238,238,241,0.6) 55%, rgba(255,255,255,0) 75%);
  }
  .back-brand {
    position: absolute;
    left: 150px; top: 160px;
    display: flex; align-items: center; gap: 16px;
  }
  .brand-square { width: 34px; height: 34px; background: var(--navy); }
  .back-brand .brand-name {
    font-size: 40px; font-weight: 700; color: var(--navy);
    text-transform: uppercase; letter-spacing: 0.5px;
  }
  .back-web {
    position: absolute;
    left: 200px; top: 232px;
    font-size: 16px; letter-spacing: 5px; color: var(--red);
  }

  /* Front side */
  .front-mark {
    position: absolute;
    left: 36px; top: 0;
    width: 84px; height: 96px;
    background: var(--red);
  }
  .front-brand {
    position: absolute;
    left: 140px; top: 36px;
    font-size: 31px; font-weight: 700; color: var(--red);
    text-transform: uppercase;
    white-space: nowrap;
  }
  .slogan {
    position: absolute;
    left: 142px; top: 86px;
    font-size: 17px; color: var(--navy); letter-spacing: 9px;
    white-space: nowrap;
  }
  .person {
    position: absolute;
    left: 36px; top: 206px;
  }
  .person-name { font-size: 24px; font-weight: 700; color: var(--red); line-height: 1; }
  .person-title { font-size: 17px; color: var(--grey-text); margin-top: 2px; }
  .divider {
    position: absolute;
    left: 36px; right: 40px; top: 258px;
    height: 1.5px; background: var(--navy);
  }
  .address {
    position: absolute;
    right: 40px; top: 170px;
    text-align: right;
    font-size: 17px; line-height: 1.3; color: var(--grey-text);
  }
  .contacts {
    position: absolute;
    left: 36px; top: 278px;
    list-style: none;
    font-size: 18px; color: var(--grey-text); line-height: 1.45;
  }
  .contacts li { display: flex; align-items: center; gap: 10px; }
  .contacts svg { width: 16px; height: 16px; flex: none; }
</style>
</head>
<body>

  <section class="card card-back">
    <div class="world-map" role="img" aria-label="Faint grey world map in the card background"></div>
    <div class="back-brand">
      <span class="brand-square"></span>
      <span class="brand-name">Harrowgate Pumps</span>
    </div>
    <div class="back-web">www.harrowgateweb.com</div>
  </section>

  <section class="card card-front">
    <div class="front-mark"></div>
    <div class="front-brand">Harrowgate Supplies Group</div>
    <div class="slogan">Tough and Dependable</div>

    <div class="address">
      PO BOX 418<br>
      Ironwood Street<br>
      Mesa Lane, Arizona 85201
    </div>

    <div class="person">
      <div class="person-name">Daniel Reyes</div>
      <div class="person-title">Owner/President</div>
    </div>
    <div class="divider"></div>

    <ul class="contacts">
      <li>
        <svg viewBox="0 0 16 16"><rect x="4" y="1" width="8" height="14" rx="1.5" fill="none" stroke="#d0202f" stroke-width="1.6"/></svg>
        555-014-2286
      </li>
      <li>
        <svg viewBox="0 0 16 16"><path d="M2 6c0-2 3-3 6-3s6 1 6 3l-2 1-1-2H5L4 7z M4 8h8l1 6H3z" fill="#d0202f"/></svg>
        555-014-2287
      </li>
      <li>
        <svg viewBox="0 0 16 16"><rect x="1" y="3" width="14" height="10" fill="#d0202f"/><path d="M1 3l7 6 7-6" fill="none" stroke="#fff" stroke-width="1.2"/></svg>
        info@harrowgatemail.com
      </li>
    </ul>
  </section>

</body>
</html>
```